Website - Varsity Homehelpers
Varsity Homehelpers
Project: Website - Varsity Homehelpers
Website - Varsity Homehelpers - Personal Care
Creative Brief
Personal Care
www.varsityhomehelpers-example.com
Varsity Homehelpers is a student based non-medical home health care company designed to enable our clients to age safely in their own homes, while helping prepare our workers for successful careers as healthcare professionals. Our services include: Assistance with activities of daily living, medication management, hygiene monitoring, housekeeping, cooking, transportation, shopping, and companionship. The workplace is our client’s homes, where they feel safe and comfortable. Clients are cared for by college students who are studying to become future Registered Nurses, Physicians, Surgeons, Therapists, Pharmacists, Dietitians, and more. This is a rare opportunity for our clients to be cared for by highly educated and respectable individuals at a rate our competitors can not match for the service. Varsity Homehelpers was created to help our workers meet the financial demands of higher education while creating a solid foundation for professional careers in the health care industry, by enabling our clients to be more then just a patient, but also a teacher!
I would like images of: College students, graduating students, young health care professionals (doctors, nurses, ect) and active healthier looking seniors. I do not want images of seniors in wheelchairs, with walkers, or that appear as if the need help.
below header
www.dorvantix-example.com
www.quellbrook-example.com
www.fernwaymeridianholdings-example.com
The business is a combination of website url 1 & 2. I would like to incorporate concepts from both of these into my website. Has to compete in professionalism and attractiveness. I do really like the simple layout of url 3 as well though. Please use your imagination and good luck!

```html
<!DOCTYPE html>
<html lang="en">
<head>
<meta charset="utf-8">
<title>Varsity Homehelpers</title>
<link href="https://fonts.googleapis.com/css2?family=Oswald:wght@400;500&family=Open+Sans:wght@400;600;700&display=swap" rel="stylesheet">
<style>
:root{
  --brand-red:#b4271a;
  --brand-red-dark:#7d160c;
  --page-bg:#8a1d12;
  --page-bg-edge:#6e140b;
  --navy:#1f3b6e;
  --topbar:#2c3e58;
  --text:#444;
  --muted:#8a8a8a;
  --line:#e2e2e2;
  --panel:#f4f4f4;
  --white:#fff;
}
*{box-sizing:border-box;margin:0;padding:0}
html,body{width:1200px;height:1000px;overflow:hidden}
body{background:linear-gradient(90deg,var(--page-bg-edge),var(--page-bg) 12%,var(--page-bg) 88%,var(--page-bg-edge));font-family:"Open Sans",Arial,sans-serif;color:var(--text);position:relative}
.site{position:absolute;left:154px;top:0;width:900px;height:1000px;background:var(--white)}
.abs{position:absolute}

/* header */
.logo{left:30px;top:28px;display:flex;align-items:center;gap:10px}
.logo-name{font-family:"Oswald",sans-serif;font-weight:500;font-size:34px;color:var(--brand-red);letter-spacing:.5px}
.logo-dot{width:16px;height:16px;border-radius:50%;background:var(--brand-red)}
.topbar{left:620px;top:0;width:252px;height:32px;background:var(--topbar);border-radius:0 0 6px 6px;display:flex;align-items:center;padding:0 12px;gap:6px}
.social{width:15px;height:15px;background:#5e7597;border-radius:2px}
.account-links{margin-left:auto;font-size:11px;color:#dfe6f0}
.phone{right:28px;top:38px;font-size:17px;color:var(--navy)}

/* nav */
.nav{left:30px;top:113px;width:840px;height:41px;background:linear-gradient(#c53a2a,var(--brand-red-dark));display:flex;align-items:center;border-radius:2px}
.nav a{color:var(--white);text-decoration:none;font-size:16px;padding:0 22px;line-height:41px;border-right:1px solid rgba(0,0,0,.25);box-shadow:1px 0 0 rgba(255,255,255,.15)}

/* hero */
.hero{left:30px;top:157px;width:840px;height:275px;background:#eef1f3}
.hero-photo{left:0;top:0;width:520px;height:275px;background:linear-gradient(120deg,#cfe0ea,#e8d8c4 45%,#b9cfae 85%)}
.hero-dots{left:440px;top:250px;display:flex;gap:6px}
.hero-dots span{width:12px;height:12px;border-radius:50%;background:var(--navy)}
.hero-dots span:first-child{background:#97a6c0}
.audience{left:520px;width:320px;height:135px;background:linear-gradient(#fff,#eceff2);border-left:1px solid var(--line)}
.audience.students{top:0}
.audience.clients{top:138px}
.audience h3{position:absolute;left:18px;top:10px;font-family:"Oswald",sans-serif;font-weight:400;font-size:24px;color:var(--navy)}
.audience p{position:absolute;left:18px;top:48px;width:175px;font-size:11.5px;line-height:15px;color:#555}
.audience .btn{position:absolute;left:18px;top:98px;background:var(--navy);color:var(--white);font-size:12px;font-weight:700;padding:4px 12px;border-radius:2px}
.audience-photo{position:absolute;right:10px;top:8px;width:110px;height:124px;border-radius:4px}
.students .audience-photo{background:linear-gradient(#cfe3ef,#3f74b3)}
.clients .audience-photo{background:linear-gradient(#e6ddd3,#b98f73)}

/* welcome */
.welcome{left:30px;top:452px;width:840px}
.welcome h1{font-family:"Oswald",sans-serif;font-weight:400;font-size:24px;color:var(--brand-red);padding-bottom:8px;border-bottom:1px solid var(--line)}
.welcome p{margin-top:12px;font-size:13px;line-height:19px;color:#555}

/* tabs */
.tabs{left:35px;top:610px;width:572px;height:260px;border:1px solid var(--line);background:var(--panel)}
.tab-row{display:flex;height:38px;border-bottom:1px solid var(--line)}
.tab-row span{flex:1;text-align:center;line-height:38px;font-size:14px;font-weight:700;color:var(--navy)}
.tab-row span.active{background:var(--white);border-right:1px solid var(--line)}
.tab-body{position:relative;background:var(--white);margin:10px;height:200px}
.tab-photo{position:absolute;left:10px;top:14px;width:140px;height:96px;background:linear-gradient(135deg,#d8c1a8,#a98a70)}
.tab-text{position:absolute;left:168px;top:14px;width:380px;font-size:11.5px;line-height:16px;color:#555}
.tab-text strong{display:block;color:#333;margin-bottom:4px}

.testimonials{left:642px;top:610px;width:230px}
.testimonials h2{font-family:"Oswald",sans-serif;font-weight:400;font-size:22px;color:var(--brand-red);padding-bottom:6px;border-bottom:1px solid var(--line)}
.testimonials blockquote{margin-top:12px;background:var(--panel);padding:14px;font-style:italic;font-size:12.5px;line-height:18px;color:#999;height:180px}

/* footer */
.footer{left:30px;top:878px;width:840px;height:40px;background:linear-gradient(#c53a2a,var(--brand-red-dark));display:flex;align-items:center;padding-left:20px}
.footer a{color:var(--white);font-size:12px;text-decoration:none;padding:0 22px}
</style>
</head>
<body>
<div class="site">
  <header>
    <div class="abs logo"><span class="logo-name">Varsity Homehelpers</span><span class="logo-dot"></span></div>
    <div class="abs topbar">
      <span class="social"></span><span class="social"></span><span class="social"></span>
      <span class="account-links">Log in | Join Us | Help</span>
    </div>
    <div class="abs phone">Call Us Today: 1800.555.0142</div>
  </header>

  <nav class="abs nav">
    <a href="#">Home</a><a href="#">About Us</a><a href="#">Services</a><a href="#">New &amp; Events</a><a href="#">Contact Us</a>
  </nav>

  <section class="abs hero">
    <div class="abs hero-photo" role="img" aria-label="Smiling senior woman embraced by a young caregiver outdoors"></div>
    <div class="abs hero-dots"><span></span><span></span><span></span></div>
    <div class="abs audience students">
      <h3>Students</h3>
      <p>Lorem ipsum dolor sit amet, consectetur adipisicing elit, sed do eiusmod tempor</p>
      <span class="btn">Apply Now</span>
      <div class="audience-photo" role="img" aria-label="Young nurse in blue scrubs"></div>
    </div>
    <div class="abs audience clients">
      <h3>Clients</h3>
      <p>Lorem ipsum dolor sit amet, consectetur adipisicing elit, sed do eiusmod tempor</p>
      <span class="btn">Get Started</span>
      <div class="audience-photo" role="img" aria-label="Active senior couple smiling"></div>
    </div>
  </section>

  <section class="abs welcome">
    <h1>Welcome to Varsity Homehelpers</h1>
    <p>Varsity Homehelpers is a student based non-medical home health care company designed to enable our clients to age safely in their own homes, while helping prepare our workers for successful careers as healthcare professionals. Our services include: Assistance with activities of daily living, medication management, hygiene monitoring, housekeeping, cooking, transportation, shopping, and companionship. The workplace is our client's homes, where they feel safe and comfortable.</p>
  </section>

  <section class="abs tabs">
    <div class="tab-row"><span class="active">About Us</span><span>Mission</span><span>Photos</span><span>Services</span><span>Contact Us</span></div>
    <div class="tab-body">
      <div class="tab-photo" role="img" aria-label="Caregiver holding a senior's hands"></div>
      <div class="tab-text">
        <strong>Lorem ipsum dolor sit amet, consectetur adipisicing elit, sed do eiusmod tempor incididunt ut labore et</strong>
        Curabitur sed urna id nunc pulvinar semper. Nunc sit amet tortor sit amet lacus sagittis posuere cursus vitae Curabitur sed urna id nunc pulvinar semper. Nunc sit amet tortor sit amet lacus sagittis posuere cursus vitae Curabitur sed urna id nunc pulvinar semper. Nunc sit amet tortor sit amet lacus nunc.
      </div>
    </div>
  </section>

  <aside class="abs testimonials">
    <h2>Testimonials</h2>
    <blockquote>" Lorem ipsum dolor sit amet, consectetur adipisicing elit, sed do eiusmod tempor incididunt ut labore et dolore magna aliqua. Ut enim ad minim veniam. Excepteur sint occaecat cupidatat non proident. "</blockquote>
  </aside>

  <footer class="abs footer">
    <a href="#">Home</a><a href="#">Company</a><a href="#">Products</a><a href="#">Support</a><a href="#">Contact Us</a>
  </footer>
</div>
</body>
</html>
```